Yoga Training Cerificate

Design a certificate of graduation from a Vinyasa Yoga Teacher Training Program.

The attached document is an example of the certificate I received as a graduate from a teacher training program. You can use it as a template.

Stylistically, what you design can be: visually enticing, professional, clean, and modern.

Please develop the "Lumen Stretch" logo and embed it within the certificate.

Please add a circular watermark behind the body of the certificate similar to the one found in the attachment; leave out the words Asana Guildhall because I am not associated with that organization.

The name of my school is "Lumen Stretch." And it was established in 2017, which you can include.

The certificate affirms that "' 'such-and-such' has successfully completed the Lumen Stretch modern vinyasa yoga training, completing two hundred hours of instruction in practice and theory. Within the power of our institution as a certifying agent we declare Such-and-such, now, a teacher competent to share the gift of yoga with the masses in a safe and effective."

My name -Dennis Whitcombe- should be at bottom with a faux-signature; position title: Lumen Stretch founder.

If you decide to include text on the fringe, like the example, it might include bars of text describing the maxims of the Lumen Stretch school reading:

This is Lumen Stretch
Breath is primary
Evolve the physical culture
Bring your unique expression to the practice
Take Breaks
Freestyle
Close your eyes
Feel deeper into your body
This is active meditation
This is moving meditation
This is modern meditation

And find a way to integrate Emojis like: Fire, Water, Prayer Hands, etc. as you see fit.

Generally, make the certificate look: official, clear and clean. You can base it from the example given. And try and create a graphic design that is more visually capturing then the example.

```html
<!DOCTYPE html>
<html lang="en">
<head>
<meta charset="utf-8">
<title>Lumen Stretch – Certificate of Completion</title>
<link href="https://fonts.googleapis.com/css2?family=Pinyon+Script&family=Roboto:wght@400;500&family=Alegreya:ital@1&display=swap" rel="stylesheet">
<style>
  :root {
    --page-bg: #ebe8e4;
    --paper: #ffffff;
    --ink: #141414;
    --rule: #8a8a8a;
    --accent: #f7931e;
    --watermark: #fde3c8;
    --figure-top: #d4d4d6;
    --figure-bottom: rgba(230, 230, 232, 0);
  }
  * { margin: 0; padding: 0; box-sizing: border-box; }
  html, body { width: 1200px; height: 1200px; overflow: hidden; }
  body { background: var(--page-bg); position: relative; }

  .certificate {
    position: absolute;
    left: 40px; top: 167px;
    width: 1120px; height: 866px;
    background: var(--paper);
    box-shadow: 0 2px 10px rgba(0,0,0,0.12);
    overflow: hidden;
  }

  .maxims {
    position: absolute;
    left: 43px; top: 76px;
    list-style: none;
    font-family: "Roboto", sans-serif;
    font-size: 14px;
    letter-spacing: 1.6px;
    color: var(--ink);
  }
  .maxims li { height: 46.5px; line-height: 22px; padding-left: 19px; position: relative; }
  .maxims li::before {
    content: ""; position: absolute; left: 0; top: 9px;
    width: 5px; height: 5px; border-radius: 50%; background: var(--ink);
  }
  .maxims li.continued::before { display: none; }

  .figure-panel {
    position: absolute;
    left: 293px; top: 58px;
    width: 160px; height: 808px;
    background: linear-gradient(to bottom, var(--figure-top) 0%, var(--figure-top) 72%, var(--figure-bottom) 100%);
    border-radius: 40px 40px 0 0;
  }

  .elements {
    position: absolute;
    left: 38px; top: 674px;
    display: flex; gap: 9px;
  }
  .elements .element {
    width: 68px; height: 68px; border-radius: 50%;
    background: var(--accent);
    display: flex; align-items: center; justify-content: center;
  }

  .watermark {
    position: absolute;
    left: 547px; top: 300px;
    width: 452px;
    text-align: center;
    font-family: "Alegreya", serif;
    font-style: italic;
    font-size: 56px;
    line-height: 70px;
    color: var(--watermark);
  }

  .title { position: absolute; left: 440px; top: 40px; }
  .title text {
    font-family: "Pinyon Script", cursive;
    font-size: 50px;
    fill: var(--ink);
  }

  .date-line {
    position: absolute;
    left: 514px; top: 232px;
    font-family: "Alegreya", serif; font-style: italic;
    font-size: 26px; color: var(--ink);
    white-space: nowrap;
  }
  .blank { display: inline-block; border-bottom: 1.5px solid var(--ink); vertical-align: baseline; height: 1px; }

  .name-rule {
    position: absolute; left: 510px; top: 417px;
    width: 511px; height: 1px; background: var(--rule);
  }

  .statement {
    position: absolute;
    left: 447px; top: 427px;
    width: 640px;
    text-align: center;
    font-family: "Alegreya", serif; font-style: italic;
    font-size: 25px; line-height: 36px;
    color: var(--ink);
  }

  .signature-rule {
    position: absolute; left: 622px; top: 758px;
    width: 294px; height: 1px; background: var(--rule);
  }
  .signatory {
    position: absolute; left: 569px; top: 767px;
    width: 400px; text-align: center;
    font-family: "Alegreya", serif; font-style: italic;
    font-size: 34px; color: var(--ink);
  }
</style>
</head>
<body>
  <main class="certificate">
    <ul class="maxims">
      <li>This is Lumen Stretch</li>
      <li>Breath is primary</li>
      <li>Evolve the physical culture</li>
      <li>Bring your unique expression</li>
      <li class="continued">to the practice</li>
      <li>Take Breaks</li>
      <li>Freestyle</li>
      <li>Close your eyes</li>
      <li>Feel deeper into your body</li>
      <li>This is active meditation</li>
      <li>This is moving meditation</li>
      <li>This is modern meditation</li>
    </ul>

    <div class="figure-panel" role="img" aria-label="Grey silhouette of a yogi in a headstand with a fading reflection"></div>

    <div class="elements">
      <div class="element" aria-label="Fire">
        <svg width="38" height="44" viewBox="0 0 38 44"><path d="M19 2 C22 12 32 16 32 28 C32 37 26 42 19 42 C12 42 6 37 6 28 C6 21 11 17 13 11 C15 17 17 19 19 20 C20 14 18 8 19 2 Z" fill="#fff"/><path d="M19 26 C21 31 25 32 25 36 C25 39 22 41 19 41 C16 41 13 39 13 36 C13 32 17 31 19 26 Z" fill="var(--accent)"/></svg>
      </div>
      <div class="element" aria-label="Water">
        <svg width="32" height="42" viewBox="0 0 32 42"><path d="M16 2 C20 12 29 20 29 28 C29 35.5 23 40 16 40 C9 40 3 35.5 3 28 C3 20 12 12 16 2 Z" fill="#fff"/></svg>
      </div>
      <div class="element" aria-label="Prayer hands">
        <svg width="40" height="44" viewBox="0 0 40 44"><path d="M18 3 C15 8 13 18 9 26 L4 34 L10 40 L19 32 Z" fill="#fff"/><path d="M22 3 C25 8 27 18 31 26 L36 34 L30 40 L21 32 Z" fill="#fff"/></svg>
      </div>
    </div>

    <p class="watermark" aria-hidden="true">Lumen Stretch</p>

    <svg class="title" width="660" height="130" viewBox="0 0 660 130" aria-label="Certificate of Completion">
      <path id="title-arc" d="M10 100 Q 300 10 650 110" fill="none"/>
      <text><textPath href="#title-arc" textLength="630" lengthAdjust="spacing">Certificate of Completion</textPath></text>
    </svg>

    <p class="date-line">On this <span class="blank" style="width:92px"></span>day of <span class="blank" style="width:170px"></span> , <span class="blank" style="width:90px"></span></p>

    <div class="name-rule"></div>

    <p class="statement">
      'such-and-such' has successfully completed the<br>
      Lumen Stretch modern vinyasa yoga training, completing two<br>
      hundred hours of instruction in practice and theory.<br>
      Within the power of our institution as a<br>
      certifying agent we declare Such-and-such,<br>
      now, a teacher competent to share<br>
      the gift of yoga with the masses in a safe and effective
    </p>

    <div class="signature-rule"></div>
    <p class="signatory">Dennis Whitcombe</p>
  </main>
</body>
</html>
```